Menu Design Project

Hi there!

We're looking to create a kick ass menu for our new restaurant. Our restaurant will be open all day from 10Am till midnight, the kitchen does not close. We will be selling burgers, burritos, pizzas, saladas, cocktails, international beers, sandwiches, wraps.

Our restaurant it's located in Sevilla, Spain. 99% of the restaurants in Sevilla sell tapas & tradional food from Spain but we are sick of that, so we've created this restaurant!

www.lunopage.com/MoraVentaBar

We're targeting all type of people: young travelers, young locals, parents & kids, first time date, you know, everyone!

We will have:

breakfast - Brunch
Lunch & dinner
Happy hour drinks & cocktails
Sandwiches, wraps & pizzas

```html
<!DOCTYPE html>
<html lang="en">
<head>
<meta charset="utf-8">
<title>Mora Venta Bar and Restaurant – Menu</title>
<link rel="stylesheet" href="https://fonts.googleapis.com/css2?family=Bebas+Neue&family=Archivo+Narrow:wght@400;500&display=swap">
<style>
  :root {
    --backdrop: #000000;
    --paper: #ffffff;
    --orange: #f5921e;
    --red: #e4252e;
    --sky: #a9dcf1;
    --grey: #9a9a9a;
    --ink: #1d1d1d;
    --rule: rgba(255, 255, 255, 0.55);
  }
  * { box-sizing: border-box; margin: 0; padding: 0; }
  html, body { width: 1200px; height: 900px; overflow: hidden; background: var(--backdrop); }
  .canvas { position: relative; width: 1200px; height: 900px; }

  /* Roll-up banner */
  .banner { position: absolute; left: 94px; top: 14px; width: 307px; height: 870px; background: var(--paper); overflow: hidden; }
  .banner__sky { position: absolute; left: 0; top: 0; width: 100%; height: 62px; background: var(--sky); }
  .banner__brand { position: absolute; left: 16px; top: 100px; width: 276px; }
  .banner__name { font-family: "Bebas Neue", sans-serif; font-size: 66px; line-height: 1; color: var(--ink); letter-spacing: 1px; }
  .banner__tagline { font-family: "Archivo Narrow", sans-serif; font-weight: 500; font-size: 11px; color: var(--ink); text-align: right; margin-top: 26px; }
  .banner__photo { position: absolute; left: 0; top: 272px; width: 100%; height: 500px;
    background: linear-gradient(160deg, #d9cfc4 0%, #bfa98e 25%, #e7ece2 45%, #9ab46a 65%, #d79a55 85%, #f2efe9 100%); }
  .banner__dish { position: absolute; border-radius: 50%; border: 3px solid var(--red); }
  .banner__dish--steak { left: 6px; top: 686px; width: 80px; height: 80px; background: radial-gradient(#6d3d24, #3c2416); }
  .banner__dish--drink { left: 84px; top: 666px; width: 110px; height: 110px; border-color: var(--sky); background: radial-gradient(#cfe6f5, #15357a 70%); }
  .banner__dish--chicken { left: 190px; top: 664px; width: 110px; height: 110px; background: radial-gradient(#d08a45, #6f8c3c); }
  .banner__slogan { position: absolute; left: 0; top: 815px; width: 100%; text-align: center; font-family: "Bebas Neue", sans-serif; font-size: 30px; letter-spacing: 1px; color: var(--grey); }
  .banner__slogan span { color: var(--red); padding: 0 4px; }

  /* Menu sheet */
  .menu { position: absolute; left: 470px; top: 14px; width: 615px; height: 870px; background: var(--paper); }
  .menu__column { position: absolute; top: 14px; width: 278px; height: 838px; background: var(--orange); }
  .menu__column--left { left: 15px; }
  .menu__column--right { left: 322px; }
  .menu__photo { position: absolute; left: 0; width: 100%; }
  .menu__heading { position: absolute; left: 0; width: 100%; height: 32px; background: var(--red); color: #fff;
    font-family: "Bebas Neue", sans-serif; font-size: 21px; line-height: 34px; padding-left: 12px; letter-spacing: 0.5px; }
  .menu__list { position: absolute; left: 12px; width: 249px; list-style: none; font-family: "Archivo Narrow", sans-serif; font-size: 13px; color: #fff; }
  .menu__item { display: flex; justify-content: space-between; height: 20px; line-height: 20px; border-bottom: 1px dotted var(--rule); }
  .menu__list--tall .menu__item { height: 20.8px; line-height: 20.8px; }

  .happy-hour { position: absolute; left: 143px; top: 696px; width: 124px; height: 124px; border-radius: 50%;
    background: radial-gradient(circle at 45% 35%, #d6f1fb, #8fd2ee 70%); border: 3px solid #fff;
    display: flex; flex-direction: column; align-items: center; justify-content: center;
    font-family: "Bebas Neue", sans-serif; color: #fff; line-height: 0.95; }
  .happy-hour__label { font-size: 22px; }
  .happy-hour__offer { font-size: 34px; }
</style>
</head>
<body>
<div class="canvas">

  <section class="banner">
    <div class="banner__sky"></div>
    <div class="banner__brand">
      <div class="banner__name">Mora Venta</div>
      <div class="banner__tagline">Bar and Restaurant</div>
    </div>
    <div class="banner__photo" role="img" aria-label="Close-up photo of a fresh salad with grilled prawns and a glass behind"></div>
    <div class="banner__dish banner__dish--steak" role="img" aria-label="Photo of grilled steak with vegetables"></div>
    <div class="banner__dish banner__dish--drink" role="img" aria-label="Photo of a splashing cocktail glass"></div>
    <div class="banner__dish banner__dish--chicken" role="img" aria-label="Photo of roast chicken with salad"></div>
    <div class="banner__slogan">Eat <span>|</span> Drink <span>|</span> Relax</div>
  </section>

  <section class="menu">
    <div class="menu__column menu__column--left">
      <div class="menu__photo" style="top:0;height:137px;background:linear-gradient(180deg,#c9382e 0%,#e9e3d8 40%,#c7823a 75%,#f3efe8 100%);" role="img" aria-label="Photo of a full cooked breakfast plate"></div>
      <h2 class="menu__heading" style="top:137px;">Breakfast</h2>
      <ul class="menu__list" style="top:180px;">
        <li class="menu__item"><span>Fry (10 pieces)</span><span>£6.00</span></li>
        <li class="menu__item"><span>Mini Fry (5 pieces)</span><span>£5.00</span></li>
        <li class="menu__item"><span>Full Soda</span><span>£4.00</span></li>
        <li class="menu__item"><span>Bacon Soda or Bap</span><span>£4.00</span></li>
        <li class="menu__item"><span>Sausage Soda or Bap</span><span>£4.00</span></li>
        <li class="menu__item"><span>Children's Breakfast (4 pieces)</span><span>£4.00</span></li>
        <li class="menu__item"><span>Sausage Egg Soda or Bap</span><span>£4.00</span></li>
        <li class="menu__item"><span>Bacon Egg Soda or Bap</span><span>£4.00</span></li>
        <li class="menu__item"><span>Scrambled Egg &amp; Toast</span><span>£4.00</span></li>
        <li class="menu__item"><span>Scrambled Egg Toast Bacon</span><span>£4.00</span></li>
      </ul>
      <h2 class="menu__heading" style="top:397px;">Lunch</h2>
      <ul class="menu__list" style="top:448px;">
        <li class="menu__item"><span>Chipotle Chicken Wrap</span><span>£8.95</span></li>
        <li class="menu__item"><span>Mediterranean Chicken Wrap</span><span>£9.95</span></li>
        <li class="menu__item"><span>Turkey Avocado Wrap</span><span>£8.95</span></li>
        <li class="menu__item"><span>Sammy's Rib Eye Steak Sandwich</span><span>£5.95</span></li>
        <li class="menu__item"><span>Chicken Club</span><span>£12.95</span></li>
        <li class="menu__item"><span>Blackened Salmon Sandwich</span><span>£14.95</span></li>
        <li class="menu__item"><span>Grilled Veggie Sandwich</span><span>£11.95</span></li>
        <li class="menu__item"><span>Ahi Tuna Steak Sandwich</span><span>£15.95</span></li>
        <li class="menu__item"><span>The Club</span><span>£12.95</span></li>
        <li class="menu__item"><span>Turkey Avocado Swiss Panini</span><span>£10.95</span></li>
        <li class="menu__item"><span>Greek Style Chicken Panini</span><span>£11.95</span></li>
        <li class="menu__item"><span>Club Panini</span><span>£10.95</span></li>
      </ul>
      <div class="menu__photo" style="top:705px;height:133px;background:linear-gradient(180deg,#7a5630 0%,#9dbb45 45%,#c9864a 70%,#2f4f86 100%);" role="img" aria-label="Photo of wraps on a green plate on a tiled table"></div>
    </div>

    <div class="menu__column menu__column--right">
      <div class="menu__photo" style="top:0;height:137px;background:linear-gradient(160deg,#b83224 0%,#d9783a 40%,#e9b45a 65%,#8c3a22 100%);" role="img" aria-label="Photo of a pizza with olives and peppers"></div>
      <h2 class="menu__heading" style="top:137px;">Diner</h2>
      <ul class="menu__list menu__list--tall" style="top:182px;">
        <li class="menu__item"><span>Margherita</span><span>£13.95</span></li>
        <li class="menu__item"><span>BBQ Chicken</span><span>£14.95</span></li>
        <li class="menu__item"><span>Chicken Cordon Bleu</span><span>£13.95</span></li>
        <li class="menu__item"><span>The OMG! Burger</span><span>£10.95</span></li>
        <li class="menu__item"><span>½ lb Angus Bacon Cheese Burger</span><span>£14.95</span></li>
        <li class="menu__item"><span>Chef's Special recipe</span><span>£16.95</span></li>
        <li class="menu__item"><span>The Monster Burger!</span><span>£14.95</span></li>
      </ul>
      <h2 class="menu__heading" style="top:344px;">Cocktails</h2>
      <ul class="menu__list menu__list--tall" style="top:397px;">
        <li class="menu__item"><span>Blue Martini</span><span>£9.80</span></li>
        <li class="menu__item"><span>Nuclear Daiquiri</span><span>£8.20</span></li>
        <li class="menu__item"><span>Rapaska</span><span>£7.90</span></li>
        <li class="menu__item"><span>Banana Wacky Baccy</span><span>£8.20</span></li>
        <li class="menu__item"><span>Absolutely Crushed</span><span>£8.00</span></li>
        <li class="menu__item"><span>Kool Hand Luke</span><span>£7.90</span></li>
        <li class="menu__item"><span>Jack Harbour Sour</span><span>£8.20</span></li>
        <li class="menu__item"><span>Ching</span><span>£7.90</span></li>
        <li class="menu__item"><span>Mexican Butterfly</span><span>£8.00</span></li>
        <li class="menu__item"><span>Tiramisu</span><span>£8.20</span></li>
        <li class="menu__item"><span>Coral</span><span>£8.20</span></li>
        <li class="menu__item"><span>Parma Violet</span><span>£8.20</span></li>
        <li class="menu__item"><span>Selection of Beer</span><span>£4.00</span></li>
      </ul>
      <div class="menu__photo" style="top:707px;height:131px;background:linear-gradient(90deg,#2a1a14 0%,#b9c86a 30%,#5a2e1e 60%,#241510 100%);" role="img" aria-label="Photo of an iced mojito cocktail at a bar"></div>
      <div class="happy-hour">
        <span class="happy-hour__label">Happy Hour</span>
        <span class="happy-hour__offer">2 for 1</span>
      </div>
    </div>
  </section>

</div>
</body>
</html>
```